Business Card Design Project

New business cards that encompass our new logo.
Looking for -
Name, Title, Cell Phone, Email, Address (2 lines), Main Phone, Fax, and website.
Reason: I don't like the graphics used to show phone, fax, cell, email, web, and address.....
I like the double sided cards with logo's on the back. I do not like the logos for phone, fax, cell, address, email, or web.

```html
<!DOCTYPE html>
<html lang="en">
<head>
<meta charset="utf-8">
<title>Northpeak Kitchen Supply – Business Card</title>
<link href="https://fonts.googleapis.com/css2?family=Montserrat:wght@400;500;700&display=swap" rel="stylesheet">
<style>
  :root {
    --backdrop: #2e2e2e;
    --card: #ffffff;
    --brand-red: #c33a4a;
    --brand-blue: #1f3f7a;
    --card-shadow: rgba(0, 0, 0, 0.45);
  }
  * { margin: 0; padding: 0; box-sizing: border-box; }
  html, body {
    width: 1200px;
    height: 900px;
    overflow: hidden;
    background: var(--backdrop);
    font-family: "Montserrat", Arial, sans-serif;
  }
  .stage {
    position: relative;
    width: 1200px;
    height: 900px;
  }
  .card {
    position: absolute;
    top: 301px;
    width: 515px;
    height: 297px;
    background: var(--card);
    box-shadow: 0 4px 10px var(--card-shadow);
    overflow: hidden;
  }
  .card--front { left: 72px; }
  .card--back { left: 615px; }

  .brand-name {
    position: absolute;
    top: 58px;
    right: 34px;
    width: 180px;
    color: var(--brand-blue);
    font-weight: 700;
    font-size: 19px;
    letter-spacing: 0.5px;
    line-height: 23px;
    text-align: right;
  }

  .person {
    position: absolute;
    left: 34px;
    top: 84px;
    color: var(--brand-red);
    font-weight: 500;
    font-size: 13.5px;
    line-height: 19px;
  }

  .contact-list {
    position: absolute;
    left: 34px;
    top: 149px;
    list-style: none;
    color: var(--brand-blue);
    font-size: 12.5px;
    line-height: 17.5px;
  }
  .contact-list .label {
    color: var(--brand-red);
    display: inline-block;
    width: 16px;
  }

  .address {
    position: absolute;
    left: 34px;
    top: 225px;
    color: var(--brand-blue);
    font-style: normal;
    font-size: 12.5px;
    line-height: 17.5px;
  }

  .back-brand {
    position: absolute;
    inset: 0;
    display: flex;
    align-items: center;
    justify-content: center;
    gap: 14px;
    color: var(--brand-red);
    font-weight: 700;
    font-size: 26px;
    letter-spacing: 1px;
  }
  .back-brand .mark-square {
    width: 22px;
    height: 22px;
    background: var(--brand-red);
  }
</style>
</head>
<body>
<main class="stage">
  <section class="card card--front" aria-label="Business card front">
    <div class="brand-name">NORTHPEAK KITCHEN SUPPLY</div>

    <p class="person">
      <span class="person-name">Daniel Morrow</span><br>
      <span class="person-title">managing director</span>
    </p>

    <ul class="contact-list">
      <li><span class="label">P</span>555 210 40 17</li>
      <li><span class="label">M</span>555 318 62 09</li>
      <li><span class="label">E</span>dmorrow@northpeaksupply.com</li>
    </ul>

    <address class="address">
      48 Harbor Lane<br>
      Millbrook, New York 12545<br>
      www.NorthpeakSupply.com
    </address>
  </section>

  <section class="card card--back" aria-label="Business card back">
    <div class="back-brand">
      <span class="mark-square"></span>
      <span>NORTHPEAK KITCHEN SUPPLY</span>
    </div>
  </section>
</main>
</body>
</html>
```